Poster Design - Stand Up Paddle Eco Tour

We need a A3 size poster design (using Adobe Illustrator) for our company's stand up paddle tour. Our tour is on flat water, calm and safe, suitable for all ages and level.

WE provide worldclass SUP boards for our customers. And branded Joren Maltby life jacket. Our instructors are all well trained and exeprience. Plus they are super friendly. Every paddling trip come with a safety boat.

Please refer to attached files for text and photos.

Our website is www.brinkwaveoar.com.sg

IMPORTANT NOTE - The design has to be done in Adobe Illustrator. The winning designer has to submit the working file in Adobe Illustrator.

Target Market(s)

Working adult - 20 - 35 year old

Industry/Entity Type

Tourism

Requirements
Must have
• The project MUST be done in Adobe Illustrator and the winning designer has to submit the artwork to us in Adobe Illustrator format.
Nice to have
• pleasant to look at.

```html
<!DOCTYPE html>
<html lang="en">
<head>
<meta charset="UTF-8">
<title>Brinkwave Oar – SUP &amp; Eco Tour Poster</title>
<link href="https://fonts.googleapis.com/css2?family=Oswald:wght@500;700&family=Roboto+Condensed:wght@400;700&display=swap" rel="stylesheet">
<style>
  :root {
    --navy: #2a3646;
    --yellow: #fdd616;
    --white: #ffffff;
    --frame: #1c1c1c;
    --grey-text: #5d6772;
    --backdrop: #e9ecec;
    --photo-dark: #3f4241;
    --photo-light: #7e8281;
  }
  * { margin: 0; padding: 0; box-sizing: border-box; }
  html, body {
    width: 960px; height: 1200px; overflow: hidden;
    background: var(--backdrop);
  }
  .poster {
    position: absolute; left: 70px; top: 20px;
    width: 820px; height: 1160px;
    background: var(--yellow);
    border: 8px solid var(--frame);
  }
  .sheet {
    position: absolute; inset: 26px 24px 30px 24px;
    background: var(--white);
  }
  .panel {
    position: absolute; left: 44px; right: 44px; top: 96px; bottom: 40px;
    border: 6px solid var(--navy);
    display: flex; flex-direction: column; align-items: center;
    text-align: center; color: var(--navy);
  }
  .brand {
    position: absolute; top: -52px; left: 50%; transform: translateX(-50%);
    background: var(--white); padding: 6px 26px 10px;
    font-family: "Oswald", sans-serif; font-weight: 700;
    font-size: 44px; line-height: 1.0; color: var(--navy);
    letter-spacing: 2px; white-space: nowrap;
  }
  .headline {
    margin-top: 40px;
    font-family: "Oswald", sans-serif; font-weight: 700;
    font-size: 170px; line-height: 0.9; letter-spacing: 1px;
  }
  .subhead {
    font-family: "Oswald", sans-serif; font-weight: 700;
    font-size: 17.5px; line-height: 1.1; margin-top: 6px; letter-spacing: 0.2px;
  }
  .subhead-large {
    font-family: "Oswald", sans-serif; font-weight: 700;
    font-size: 41px; line-height: 1.05;
  }
  .intro {
    font-family: "Roboto Condensed", sans-serif; font-size: 20px;
    color: var(--grey-text); line-height: 1.2; margin-top: 8px;
  }
  .cta-bar {
    margin-top: 12px; background: var(--navy); color: var(--white);
    font-family: "Oswald", sans-serif; font-weight: 700;
    font-size: 28px; letter-spacing: 0.5px; line-height: 1;
    padding: 8px 18px; width: calc(100% - 60px);
  }
  .details {
    font-family: "Roboto Condensed", sans-serif; font-size: 14.5px;
    color: var(--grey-text); line-height: 1.3; margin-top: 10px; padding: 0 40px;
  }
  .timing {
    margin-top: 10px; width: calc(100% - 60px);
    border-top: 2px solid var(--navy); border-bottom: 2px solid var(--navy);
    font-family: "Oswald", sans-serif; font-weight: 700;
    font-size: 22px; line-height: 1.3; padding: 2px 0;
  }
  .location {
    margin-top: 6px;
    font-family: "Roboto Condensed", sans-serif; font-weight: 700; font-size: 18px;
  }
  .location-note {
    font-family: "Roboto Condensed", sans-serif; font-size: 12px; color: var(--grey-text);
  }
  .tour-photo {
    margin-top: 10px; width: 100%; flex: 1;
    background: linear-gradient(180deg, var(--photo-dark) 0%, var(--photo-light) 100%);
  }
  .booking-strip {
    margin-top: 18px; background: var(--yellow); color: var(--navy);
    font-family: "Oswald", sans-serif; font-weight: 700;
    font-size: 19px; padding: 6px 22px; line-height: 1.1;
  }
  .web-line {
    margin-top: 12px; display: flex; align-items: center; gap: 8px;
    font-family: "Roboto Condensed", sans-serif; font-size: 18px; letter-spacing: 2px;
  }
  .dot { width: 16px; height: 16px; border-radius: 50%; background: var(--yellow); display: inline-block; }
  .web-line .gap { width: 10px; }
  .booking-contact {
    margin: 8px 0 18px;
    font-family: "Oswald", sans-serif; font-weight: 500; font-size: 24px;
  }
</style>
</head>
<body>
  <div class="poster">
    <div class="sheet">
      <section class="panel">
        <div class="brand">BRINKWAVE OAR</div>
        <h1 class="headline">EXPLORE</h1>
        <p class="subhead">THE NATURAL COASTAL SURROUNDINGS AND WATERWAYS OF JOHOR ON</p>
        <p class="subhead-large">A SUP ADVENTURE TOURING BOARD</p>
        <p class="intro">Our tours are flat-water and appropriate for all ages and levels.<br>We have the best possible service and equipment.</p>
        <p class="cta-bar">JOIN US FOR A FUN AND RELAXING DAY.</p>
        <p class="details">What could be better than a group guided tour? With life vests and a safety boat for our guided tour, you can be assured of a secured environment while you focus on just having fun and creating life's best memories with friends and family.</p>
        <p class="timing">TIMING: MORNING, AFTERNOON, AND SUNSET SESSION</p>
        <p class="location">Location: Sungai Redan, set off from Teluk Senari, Tanjung Murai.</p>
        <p class="location-note">(next to Pantai Lamar)</p>
        <div class="tour-photo" role="img" aria-label="Photo of two paddlers on touring boards on a calm mangrove-lined river"></div>
        <p class="booking-strip">CONTACT US FOR BOOKING. WE DO NOT ACCEPT WALK-IN.</p>
        <p class="web-line"><span class="dot"></span>www.brinkwaveoar.com.sg<span class="gap"></span><span class="dot"></span>brinkwave oar</p>
        <p class="booking-contact">BOOKING CONTACT: BOOKING@BRINKWAVEOAR.COM.SG</p>
      </section>
    </div>
  </div>
</body>
</html>
```